Consultancy Report Template in Word (Preferably in Google Docs)

I require a professional Google Doc Template that I will use for Professional Consultancy reports.
Using the brand guidelines attached as a base, I'd like the report themed in the brand colours.
It must look professional but I'd like some creative licence to be shown.
Feel free to pull some sample images from the website - www.vantrelo.com.au that I can replace with site specific images on the cover and within the template.
As a minimum, it must have:
Very presentable cover page
Table of contents (set up linked to headers)
Section Headings - (SECTION NAME) potentially Full Page 'semi-cover pages' or presentable banners
Sub Section Headings ( 1 - TOPIC XXX)
Sub Clauses (1.1 - TOPIC XXX)
Presentable Tables in brand colours that can be expanded to more or fewer columns and rows.
Rear Cover Page
Headers and footers

```html
<!DOCTYPE html>
<html lang="en">
<head>
<meta charset="utf-8">
<title>Vantrelo Septics Australia – Report Template</title>
<link href="https://fonts.googleapis.com/css2?family=Montserrat:wght@400;500;600;700&display=swap" rel="stylesheet">
<style>
  :root{
    --canvas:#e4e5ea;
    --paper:#f4f4f7;
    --purple:#6a4a9a;
    --purple-soft:#8a6cb4;
    --blue:#3f7fbf;
    --blue-soft:#6fa6d6;
    --sky:#a9cde9;
    --lavender:#c3b3e0;
    --ink:#4a4a58;
    --rule:#b8bfd6;
  }
  *{box-sizing:border-box;margin:0;padding:0}
  html,body{width:1200px;height:800px;overflow:hidden}
  body{background:var(--canvas);font-family:"Montserrat",sans-serif;color:var(--ink);position:relative}
  .defs{position:absolute;width:0;height:0}
  .page{position:absolute;background:var(--paper);overflow:hidden;box-shadow:0 2px 8px rgba(60,60,90,.18)}
  .wave-top{position:absolute;left:0;top:0;width:100%;height:34px}
  .wave-bottom{position:absolute;left:0;width:100%}
  .page-header{position:absolute;left:0;right:0;top:28px;height:16px}
  .page-header .dot{position:absolute;left:42px;top:0;width:14px;height:14px;border-radius:50%;border:2px solid var(--purple-soft)}
  .page-header .brand{position:absolute;left:62px;top:3px;font-size:7.6px;letter-spacing:.3px;color:var(--purple-soft);white-space:nowrap}
  .page-header .rule{position:absolute;left:62px;right:0;top:15px;border-top:1px solid var(--rule)}
  .page-footer{position:absolute;left:0;right:0;bottom:10px;font-size:6px;letter-spacing:.3px;color:var(--purple-soft);text-align:center}
  .page-footer .num{position:absolute;right:26px;color:var(--blue)}
  .photo{position:absolute}
  .brand-block{position:absolute;left:0;right:0;text-align:center;color:var(--purple-soft);font-weight:500;letter-spacing:.6px;line-height:1.1}
  .brand-mark{position:absolute;border-radius:50%;border:5px solid var(--purple-soft)}
  .contents-title{position:absolute;font-size:20px;font-weight:600;color:var(--purple);letter-spacing:.4px}
  .toc{position:absolute;right:40px}
  .toc-row{display:flex;align-items:baseline;white-space:nowrap;position:absolute;left:0;right:0}
  .toc-row .lead{flex:1;border-bottom:1px dotted #9aa0b8;margin:0 3px;transform:translateY(-2px)}
  .toc-section{font-size:11px;color:var(--ink);font-weight:500}
  .toc-section .n{color:var(--blue);margin-right:4px}
  .toc-topic{font-size:8px;color:var(--blue-soft)}
  .toc-topic .n{color:var(--ink);margin-right:6px}
  .toc-row .pg{color:var(--blue)}
  .bar{position:absolute;left:0;height:18px;background:linear-gradient(90deg,var(--blue-soft),rgba(169,205,233,.4))}
  .heading{position:absolute;color:var(--blue);font-weight:500;white-space:nowrap}
  .subheading{position:absolute;font-size:11px;color:var(--ink);font-weight:500}
  .body-copy{position:absolute;font-size:5px;line-height:1.45;color:#585866}
  .sample-table{position:absolute;border-collapse:collapse;font-size:4.6px;color:#6a6a78}
  .sample-table th{background:linear-gradient(90deg,var(--blue-soft),var(--purple-soft));color:#fff;font-weight:500;padding:5px 4px;text-align:left}
  .sample-table td{border:1px solid #cfd3e2;padding:4px 8px}
  .cover-title{position:absolute;left:0;right:0;text-align:center;font-size:22px;font-weight:700;color:var(--purple);letter-spacing:.6px}
  .prepared{position:absolute;left:0;right:0;font-size:8.5px;color:var(--ink)}
  .prepared div{display:flex;height:15px}
  .prepared .k{width:158px;text-align:right;padding-right:10px}
  .url{position:absolute;left:0;right:0;text-align:center;font-size:7px;color:var(--purple-soft);letter-spacing:.3px}
</style>
</head>
<body>

<svg class="defs" aria-hidden="true">
  <defs>
    <linearGradient id="band" x1="0" x2="1"><stop offset="0" stop-color="#a9cde9"/><stop offset="1" stop-color="#c3b3e0"/></linearGradient>
    <linearGradient id="bandDeep" x1="0" x2="1"><stop offset="0" stop-color="#6fa6d6"/><stop offset="1" stop-color="#9b86c9"/></linearGradient>
    <linearGradient id="site" x1="0" y1="0" x2="0" y2="1"><stop offset="0" stop-color="#c4d8e8"/><stop offset=".45" stop-color="#9aa98a"/><stop offset="1" stop-color="#a38c6a"/></linearGradient>
  </defs>
</svg>

<!-- Cover -->
<section class="page cover" style="left:98px;top:52px;width:330px;height:409px">
  <svg class="wave-top" viewBox="0 0 100 12" preserveAspectRatio="none"><path d="M0 0H100V10C75 2 45 9 20 6 12 5 5 4 0 4Z" fill="url(#band)" opacity=".55"/><path d="M0 0H100V4C70 6 40 2 0 3Z" fill="url(#band)"/></svg>
  <div class="brand-mark" style="left:140px;top:41px;width:56px;height:56px"></div>
  <div class="brand-block" style="top:112px;font-size:12px">VANTRELO SEPTICS<br>AUSTRALIA</div>
  <h1 class="cover-title" style="top:166px">REPORT TITLE</h1>
  <div class="prepared" style="top:208px">
    <div><span class="k">Prepared for</span><span>Client Name</span></div>
    <div><span class="k">Prepared by:</span><span>Your Company</span></div>
    <div style="margin-top:3px"><span class="k">Date:</span><span>April 2024</span></div>
  </div>
  <svg class="photo" role="img" aria-label="Site photo: septic tanker truck beside a green tank on a dirt work site" style="left:0;top:250px;width:330px;height:140px" viewBox="0 0 330 140" preserveAspectRatio="none">
    <path d="M0 40C80 10 200 15 330 40V140H0Z" fill="url(#site)"/>
    <path d="M0 20C90 0 220 30 330 0V20C230 40 100 20 0 45Z" fill="url(#band)" opacity=".9"/>
    <path d="M0 45C60 25 120 30 160 40 110 32 50 38 0 70Z" fill="url(#bandDeep)" opacity=".6"/>
  </svg>
  <div class="url" style="bottom:10px">www.vantrelo.com.au</div>
</section>

<!-- Contents -->
<section class="page contents" style="left:451px;top:52px;width:311px;height:409px">
  <svg class="wave-top" viewBox="0 0 100 12" preserveAspectRatio="none"><path d="M0 0H100V10C75 2 45 9 20 6 12 5 5 4 0 4Z" fill="url(#band)" opacity=".55"/><path d="M0 0H100V4C70 6 40 2 0 3Z" fill="url(#band)"/></svg>
  <header class="page-header"><span class="dot"></span><span class="brand">VANTRELO SEPTICS AUSTRALIA</span><span class="rule"></span></header>
  <h2 class="contents-title" style="left:32px;top:82px">CONTENTS</h2>
  <div class="bar" style="top:180px;width:40px"></div>
  <nav class="toc" style="left:32px;top:0;height:300px">
    <div class="toc-row toc-section" style="top:116px"><span class="n">1</span>- SECTION NAME<span class="lead"></span><span class="pg">1</span></div>
    <div class="toc-row toc-topic" style="top:139px;left:20px"><span class="n">1.1</span>TOPIC XXX<span class="lead"></span><span class="pg">2</span></div>
    <div class="toc-row toc-topic" style="top:157px;left:20px"><span class="n">1.2</span>TOPIC XXX<span class="lead"></span><span class="pg">4</span></div>
    <div class="toc-row toc-section" style="top:182px"><span class="n">2</span>- SECTION NAME<span class="lead"></span><span class="pg">2</span></div>
    <div class="toc-row toc-topic" style="top:204px;left:20px"><span class="n">1.1</span>TOPIC XXX<span class="lead"></span><span class="pg">2</span></div>
    <div class="toc-row toc-topic" style="top:222px;left:20px"><span class="n">1.2</span>TOPIC XXX<span class="lead"></span><span class="pg">4</span></div>
  </nav>
  <svg class="wave-bottom" style="top:320px;height:60px" viewBox="0 0 100 30" preserveAspectRatio="none"><path d="M0 30V18C30 8 60 26 100 6V30Z" fill="url(#band)" opacity=".45"/><path d="M0 30V14C35 10 65 22 100 12V17C65 26 35 16 0 26Z" fill="url(#bandDeep)" opacity=".8"/></svg>
  <footer class="page-footer">VANTRELO SEPTICS AUSTRALIA<span class="num">2</span></footer>
</section>

<!-- Contents with section photo -->
<section class="page contents" style="left:783px;top:52px;width:322px;height:409px">
  <svg class="wave-top" viewBox="0 0 100 12" preserveAspectRatio="none"><path d="M0 0H100V10C75 2 45 9 20 6 12 5 5 4 0 4Z" fill="url(#band)" opacity=".55"/><path d="M0 0H100V4C70 6 40 2 0 3Z" fill="url(#band)"/></svg>
  <header class="page-header"><span class="dot" style="left:30px"></span><span class="brand" style="left:50px">VANTRELO SEPTICS AUSTRALIA</span><span class="rule" style="left:50px"></span></header>
  <h2 class="contents-title" style="left:30px;top:82px">CONTENTS</h2>
  <div class="bar" style="top:114px;width:38px"></div>
  <nav class="toc" style="left:30px;top:0;height:300px;right:34px">
    <div class="toc-row toc-section" style="top:116px;font-size:12px"><span class="n">1</span>— SECTION NAME<span class="lead"></span><span class="pg" style="font-size:8px">1</span></div>
    <div class="toc-row toc-topic" style="top:139px;left:26px"><span class="n">1.1</span>TOPIC XXX<span class="lead"></span><span class="pg">2</span></div>
    <div class="toc-row toc-topic" style="top:157px;left:26px"><span class="n">1.2</span>TOPIC XXX<span class="lead"></span><span class="pg">4</span></div>
  </nav>
  <svg class="photo" role="img" aria-label="Section photo: vacuum tanker trucks and green tanks on a site" style="left:0;top:186px;width:322px;height:160px" viewBox="0 0 322 160" preserveAspectRatio="none">
    <path d="M0 0H322V130C250 140 120 150 0 160Z" fill="url(#site)"/>
    <path d="M280 0C240 60 220 110 170 135 220 130 260 125 322 120V135C220 140 90 150 0 160V110C60 150 180 130 220 90 250 60 265 20 280 0Z" fill="url(#bandDeep)" opacity=".7"/>
    <path d="M0 130C80 150 200 130 322 135V160H0Z" fill="var(--paper)"/>
  </svg>
  <footer class="page-footer">VANTRELO SEPTICS AUSTRALIA<span class="num">3</span></footer>
</section>

<!-- Section page -->
<section class="page section" style="left:98px;top:477px;width:290px;height:256px">
  <svg class="wave-top" style="height:22px" viewBox="0 0 100 12" preserveAspectRatio="none"><path d="M0 0H100V10C75 2 45 9 20 6 12 5 5 4 0 4Z" fill="url(#band)" opacity=".55"/><path d="M0 0H100V4C70 6 40 2 0 3Z" fill="url(#band)"/></svg>
  <header class="page-header" style="top:25px"><span class="dot" style="left:28px;width:13px;height:13px"></span><span class="brand" style="left:47px;font-size:7px">VANTRELO SEPTICS AUSTRALIA</span><span class="rule" style="left:47px"></span></header>
  <div class="bar" style="top:211px;display:none"></div>
  <div class="bar" style="top:61px;width:40px;height:16px"></div>
  <div class="heading" style="left:28px;top:61px;font-size:13.5px">1 — TOPIC XXX</div>
  <div class="subheading" style="left:28px;top:90px">1.1&nbsp; TOPIC XXX</div>
  <svg class="photo" role="img" aria-label="Photo: blue loader and green tanks at a work site" style="left:0;top:100px;width:290px;height:130px" viewBox="0 0 290 130" preserveAspectRatio="none">
    <path d="M290 0V110H60C120 95 140 60 170 30 200 8 250 2 290 0Z" fill="url(#site)"/>
    <path d="M0 95C80 110 130 70 160 40 190 12 240 4 290 2V8C240 10 200 20 175 45 140 85 90 115 0 115Z" fill="url(#bandDeep)" opacity=".55"/>
    <path d="M0 110C100 125 200 100 290 105V130H0Z" fill="url(#band)" opacity=".75"/>
  </svg>
  <p class="body-copy" style="left:28px;top:115px;width:140px">Lorem ipsum dolor sit amet, consectetur adipiscing elit, sed do eiusmod tempor incididunt ut labore et dolore magna aliqua. Ut enim ad minim veniam, quis nostrud exercitation ullamco laboris nisi ut aliquip ex ea commodo consequat.</p>
  <footer class="page-footer" style="bottom:8px">VANTRELO SEPTICS AUSTRALIA<span class="num">4</span></footer>
</section>

<!-- Table page -->
<section class="page table-page" style="left:408px;top:477px;width:225px;height:256px">
  <svg class="wave-top" style="height:22px" viewBox="0 0 100 12" preserveAspectRatio="none"><path d="M0 0H100V10C75 2 45 9 20 6 12 5 5 4 0 4Z" fill="url(#band)" opacity=".55"/><path d="M0 0H100V4C70 6 40 2 0 3Z" fill="url(#band)"/></svg>
  <header class="page-header" style="top:25px"><span class="dot" style="left:28px;width:13px;height:13px"></span><span class="brand" style="left:47px;font-size:7px">VANTRELO SEPTICS AUSTRALIA</span><span class="rule" style="left:47px"></span></header>
  <div class="bar" style="top:59px;width:40px;height:16px"></div>
  <div class="heading" style="left:24px;top:60px;font-size:12px">2.1&nbsp; SAMPLE TABLE</div>
  <p class="body-copy" style="left:26px;top:84px;width:180px">Lorem ipsum dolor sit amet, consectetur adipiscing elit, sed do eiusmod tempor incididunt ut labore et dolore magna aliqua. Ut enim ad minim veniam.</p>
  <table class="sample-table" style="left:26px;top:126px;width:183px">
    <tr><th>SAMPLE HEADER</th><th>SAMPLE HEADER</th><th>SAMPLE HEADER</th></tr>
    <tr><td>SAMPLE DATA 1</td><td>SAMPLE DATA 1</td><td>SAMPLE DATA 1</td></tr>
    <tr><td>SAMPLE DATA 1</td><td>SAMPLE DATA 2</td><td>SAMPLE DATA 2</td></tr>
    <tr><td>SAMPLE DATA 2</td><td>SAMPLE DATA 3</td><td>SAMPLE DATA 3</td></tr>
    <tr><td>SAMPLE DATA 3</td><td>SAMPLE DATA 3</td><td>SAMPLE DATA 4</td></tr>
  </table>
  <svg class="wave-bottom" style="top:215px;height:22px" viewBox="0 0 100 30" preserveAspectRatio="none"><path d="M0 30V14C35 4 65 24 100 10V16C65 30 35 12 0 24Z" fill="url(#bandDeep)" opacity=".6"/></svg>
  <footer class="page-footer" style="bottom:8px">VANTRELO SEPTICS AUSTRALIA<span class="num">2</span></footer>
</section>

<!-- Text page -->
<section class="page text-page" style="left:654px;top:477px;width:191px;height:256px">
  <svg class="wave-top" style="height:22px" viewBox="0 0 100 12" preserveAspectRatio="none"><path d="M0 0H100V10C75 2 45 9 20 6 12 5 5 4 0 4Z" fill="url(#band)" opacity=".55"/><path d="M0 0H100V4C70 6 40 2 0 3Z" fill="url(#band)"/></svg>
  <header class="page-header" style="top:25px"><span class="dot" style="left:23px;width:13px;height:13px"></span><span class="brand" style="left:41px;font-size:6.4px">VANTRELO SEPTICS AUSTRALIA</span><span class="rule" style="left:41px"></span></header>
  <div class="bar" style="top:59px;width:40px;height:14px"></div>
  <div class="heading" style="left:24px;top:59px;font-size:11px">2.1&nbsp; SAMPLE TABLE</div>
  <p class="body-copy" style="left:24px;top:82px;width:150px">Lorem ipsum dolor sit amet, consectetur adipiscing elit, sed do eiusmod tempor incididunt ut labore et dolore magna aliqua. Ut enim ad minim veniam, quis nostrud exercitation ullamco laboris nisi ut aliquip ex ea commodo consequat.</p>
  <p class="body-copy" style="left:24px;top:118px;width:150px">Lorem ipsum dolor sit amet, consectetur adipiscing elit, sed do eiusmod tempor incididunt ut labore et dolore magna aliqua. Ut enim ad minim veniam.</p>
  <svg class="wave-bottom" style="top:172px;height:40px" viewBox="0 0 100 30" preserveAspectRatio="none"><path d="M0 30V18C30 8 60 26 100 6V30Z" fill="url(#band)" opacity=".4"/><path d="M0 30V12C35 8 65 20 100 10V15C65 24 35 14 0 22Z" fill="url(#bandDeep)" opacity=".6"/></svg>
  <footer class="page-footer" style="bottom:8px">VANTRELO SEPTICS AUSTRALIA<span class="num">3</span></footer>
</section>

<!-- Rear cover -->
<section class="page rear-cover" style="left:866px;top:477px;width:239px;height:256px">
  <svg class="wave-top" style="height:22px" viewBox="0 0 100 12" preserveAspectRatio="none"><path d="M0 0H100V10C75 2 45 9 20 6 12 5 5 4 0 4Z" fill="url(#band)" opacity=".55"/><path d="M0 0H100V4C70 6 40 2 0 3Z" fill="url(#band)"/></svg>
  <div class="brand-mark" style="left:92px;top:35px;width:54px;height:54px"></div>
  <div class="brand-block" style="top:105px;font-size:11.5px">VANTRELO SEPTICS<br>AUSTRALIA</div>
  <svg class="wave-bottom" style="top:180px;height:76px" viewBox="0 0 100 40" preserveAspectRatio="none">
    <path d="M0 12C30 2 60 20 100 8V40H0Z" fill="url(#band)" opacity=".6"/>
    <path d="M0 22C35 10 65 16 100 14V40H0Z" fill="url(#bandDeep)"/>
    <path d="M0 30C30 20 60 18 100 18" stroke="#fff" stroke-width=".5" fill="none" opacity=".8"/>
  </svg>
  <div class="url" style="bottom:10px;color:#fff">www.vantrelo.com.au</div>
</section>

</body>
</html>
```